Apply color filter to a number of images to match a stylised existing design

I have an existing website design that I like. www.fernquilo.com. The blue pictures were all done previously and I do not have access to the people or process. Working on a new website and I need to process some screenshots in a similar stylised way. One test image is attached. The winning design/process will then process about 10 images for me.

```html
<!DOCTYPE html>
<html lang="en">
<head>
<meta charset="utf-8">
<title>FernquiloFly Live Video</title>
<link rel="stylesheet" href="https://fonts.googleapis.com/css2?family=Roboto:wght@400;500&family=Roboto+Condensed:wght@400&display=swap">
<style>
  :root {
    --sea-deep: #1b5893;
    --sea-mid: #2467a6;
    --sea-light: #3a80bf;
    --beach: #6aa6d8;
    --sand: #8fbde4;
    --bar-light: #c4def4;
    --bar-mid: #9fc7ea;
    --panel: rgba(28, 84, 140, 0.92);
    --panel-line: #8fc0ea;
    --text-light: #e4f2ff;
    --text-soft: #b9d9f4;
    --text-dark: #1d4e82;
    --control-dark: #143f6b;
    --white: #f3f9ff;
  }
  * { box-sizing: border-box; margin: 0; padding: 0; }
  html, body { width: 1200px; height: 675px; overflow: hidden; }
  body { font-family: "Roboto", Arial, sans-serif; color: var(--text-light); background: var(--sea-mid); }

  .screen { position: relative; width: 1200px; height: 675px; overflow: hidden; }

  .aerial-view {
    position: absolute; inset: 0;
    background: linear-gradient(180deg, var(--sea-deep) 0%, var(--sea-mid) 45%, var(--sea-light) 72%, var(--beach) 84%, var(--sand) 100%);
  }

  .title-bar {
    position: absolute; left: 0; top: 0; width: 1200px; height: 18px;
    background: var(--bar-light); color: var(--text-dark);
    font-size: 10px; line-height: 18px; padding-left: 8px;
  }

  .side-menu { position: absolute; left: 0; top: 26px; width: 124px; }
  .side-menu .menu-item {
    height: 22px; line-height: 22px; padding-left: 6px;
    background: var(--bar-light); color: var(--text-dark);
    font-size: 11px; border-bottom: 1px solid var(--bar-mid);
  }
  .side-menu .menu-head { height: 14px; line-height: 14px; font-size: 9px; text-align: center; padding: 0; }
  .side-menu .menu-debug { margin-top: 40px; }

  .flight-mode { position: absolute; left: 132px; top: 42px; font-size: 25px; color: var(--text-light); }
  .flight-mode .mode-state { margin-left: 30px; padding-left: 18px; border-left: 1px solid rgba(228,242,255,.4); }

  .status-strip { position: absolute; right: 0; top: 36px; height: 40px; display: flex; align-items: center; gap: 14px; padding-right: 8px; }
  .battery-ring { width: 36px; height: 36px; border-radius: 50%; border: 3px solid var(--text-soft); display: grid; place-items: center; font-size: 14px; background: var(--control-dark); }
  .flight-time { font-size: 30px; font-weight: 500; }
  .status-icon { font-size: 13px; color: var(--text-soft); display: flex; align-items: center; gap: 4px; }
  .status-more { font-size: 24px; letter-spacing: 2px; }

  .side-icons { position: absolute; left: 22px; }

  .camera-controls { position: absolute; left: 1028px; top: 240px; }
  .lens-pill { width: 66px; height: 170px; border-radius: 33px; background: var(--control-dark); display: flex; flex-direction: column; align-items: center; padding-top: 14px; gap: 16px; }
  .lens-option { width: 48px; height: 48px; border-radius: 50%; display: grid; place-items: center; font-size: 22px; }
  .lens-option.is-active { background: #0d2f52; }
  .focus-button { margin-top: 10px; width: 66px; height: 66px; border-radius: 50%; background: var(--control-dark); display: grid; place-items: center; font-size: 22px; font-weight: 500; }
  .shutter-button { position: absolute; left: 1116px; top: 324px; width: 74px; height: 74px; border-radius: 50%; background: var(--bar-light); }

  .measurement-panel { position: absolute; left: 371px; top: 455px; width: 314px; height: 176px; background: var(--panel); }
  .panel-title { height: 20px; line-height: 20px; padding-left: 6px; font-size: 11px; color: var(--text-dark); background: var(--bar-light); }
  .mode-group { position: absolute; left: 8px; top: 32px; width: 160px; height: 116px; border: 1px solid var(--panel-line); padding: 10px 0 0 8px; }
  .mode-group .group-label { position: absolute; top: -7px; left: 6px; font-size: 9px; background: var(--panel); padding: 0 2px; }
  .mode-option { display: flex; align-items: center; gap: 9px; font-size: 12px; height: 26px; }
  .radio { width: 8px; height: 8px; border-radius: 50%; border: 1px solid var(--text-light); }
  .radio.is-checked { background: var(--text-light); }
  .readings { position: absolute; right: 10px; top: 26px; text-align: right; font-family: "Roboto Condensed", Arial, sans-serif; }
  .reading-main { font-size: 36px; line-height: 38px; }
  .reading-row { display: flex; gap: 12px; justify-content: flex-end; align-items: center; font-size: 14px; margin-top: 8px; }
  .reading-row .unit-tag { font-size: 9px; display: flex; align-items: center; gap: 4px; }
  .unit-tag::before { content: ""; width: 7px; height: 7px; background: var(--text-light); }
  .reading-total { font-size: 14px; margin-top: 2px; }

  .zoom-panel { position: absolute; left: 783px; top: 389px; width: 220px; height: 262px; background: var(--panel); border: 1px solid var(--panel-line); }
  .zoom-view { position: absolute; left: 3px; top: 22px; width: 212px; height: 214px; background: linear-gradient(180deg, var(--sea-mid), var(--sea-light)); }
  .zoom-options { position: absolute; left: 6px; bottom: 4px; right: 6px; display: flex; gap: 16px; font-size: 10px; align-items: center; }
  .zoom-options .radio { display: inline-block; margin-right: 3px; vertical-align: -1px; }
  .zoom-options .live-update { margin-left: auto; font-size: 9px; }

  .telemetry { position: absolute; left: 0; bottom: 0; height: 60px; width: 600px; }
  .back-button { position: absolute; left: 18px; bottom: 0; width: 48px; height: 58px; background: rgba(196,222,244,.35); }
  .speed { position: absolute; bottom: 32px; font-size: 18px; }
  .altitude { position: absolute; left: 130px; bottom: 4px; font-size: 24px; word-spacing: 4px; }

  .capture-info { position: absolute; right: 50px; bottom: 4px; text-align: right; font-size: 18px; line-height: 24px; }
  .capture-info .muted { color: var(--text-soft); font-size: 16px; }
  .auto-badge { position: absolute; right: 6px; bottom: 6px; width: 36px; height: 26px; border-radius: 4px; background: var(--text-light); color: var(--text-dark); font-size: 9px; display: grid; place-items: center; font-weight: 500; }
</style>
</head>
<body>
<main class="screen">
  <div class="aerial-view" role="img" aria-label="Blue-tinted aerial drone view of the sea with a swimmer, rope lines and a boat, and a beach along the bottom"></div>

  <header class="title-bar">FernquiloFly Live Video</header>

  <nav class="side-menu">
    <div class="menu-item menu-head">Dock All</div>
    <div class="menu-item">Setup</div>
    <div class="menu-item">Settings</div>
    <div class="menu-item">Drone</div>
    <div class="menu-item menu-debug">Debug</div>
  </nav>

  <div class="flight-mode">Mode<span class="mode-state">In flight</span></div>

  <div class="status-strip">
    <div class="battery-ring">73</div>
    <div class="flight-time">30'33"</div>
    <div class="status-icon">
      <svg width="22" height="16" viewBox="0 0 22 16"><g fill="#e4f2ff"><rect x="0" y="11" width="3" height="5"/><rect x="5" y="8" width="3" height="8"/><rect x="10" y="4" width="3" height="12"/><rect x="15" y="0" width="3" height="16"/></g></svg>RC
    </div>
    <div class="status-icon">
      <svg width="26" height="26" viewBox="0 0 26 26"><circle cx="13" cy="13" r="11" fill="none" stroke="#e4f2ff" stroke-width="2"/><circle cx="13" cy="13" r="4" fill="#e4f2ff"/></svg>
    </div>
    <div class="status-icon">
      <svg width="22" height="22" viewBox="0 0 22 22"><path d="M4 18 L18 4 M8 4 h10 v10" fill="none" stroke="#e4f2ff" stroke-width="2"/></svg>28
    </div>
    <div class="status-more">···</div>
  </div>

  <svg class="side-icons" style="top:300px" width="30" height="30" viewBox="0 0 30 30"><path d="M6 26 V10 M12 26 V4 M18 26 V10 M24 26 V4" stroke="#c4def4" stroke-width="2" fill="none"/></svg>
  <svg class="side-icons" style="top:382px" width="34" height="34" viewBox="0 0 34 34"><path d="M17 4 V18 M11 12 L17 18 L23 12" stroke="#e4f2ff" stroke-width="3" fill="none"/><ellipse cx="17" cy="26" rx="12" ry="4" fill="none" stroke="#e4f2ff" stroke-width="2"/></svg>

  <svg style="position:absolute;left:1138px;top:240px" width="26" height="20" viewBox="0 0 26 20"><rect x="2" y="2" width="22" height="16" rx="2" fill="none" stroke="#e4f2ff" stroke-width="2"/></svg>

  <div class="camera-controls">
    <div class="lens-pill">
      <div class="lens-option">3</div>
      <div class="lens-option is-active">1×</div>
    </div>
    <div class="focus-button">AF</div>
  </div>
  <div class="shutter-button"></div>
  <svg style="position:absolute;left:1138px;top:452px" width="26" height="24" viewBox="0 0 26 24"><rect x="1" y="1" width="24" height="22" rx="3" fill="none" stroke="#e4f2ff" stroke-width="2"/><path d="M10 7 L17 12 L10 17 Z" fill="#e4f2ff"/></svg>

  <section class="measurement-panel">
    <div class="panel-title">Measurement</div>
    <div class="mode-group">
      <span class="group-label">Measurement Mode</span>
      <div class="mode-option"><span class="radio"></span>View</div>
      <div class="mode-option"><span class="radio is-checked"></span>Explore</div>
      <div class="mode-option"><span class="radio"></span>Manual Measure</div>
      <div class="mode-option"><span class="radio"></span>Auto Measure</div>
    </div>
    <div class="readings">
      <div class="reading-main">36.2</div>
      <div class="reading-main">119</div>
      <div class="reading-row"><span class="unit-tag">MT15</span><span>33.835</span><span>4.600</span></div>
      <div class="reading-total">34146</div>
    </div>
  </section>

  <section class="zoom-panel">
    <div class="panel-title">Zoom</div>
    <div class="zoom-view" role="img" aria-label="Magnified blue-tinted view of the swimmer in the water"></div>
    <div class="zoom-options">
      <span><span class="radio is-checked"></span>x 2</span>
      <span><span class="radio"></span>x 4</span>
      <span><span class="radio"></span>x 8</span>
      <span class="live-update">Live Update</span>
    </div>
  </section>

  <div class="telemetry">
    <div class="back-button">
      <svg width="48" height="58" viewBox="0 0 48 58"><path d="M30 12 L14 29 L30 46" stroke="#e4f2ff" stroke-width="3" fill="none"/></svg>
    </div>
    <div class="speed" style="left:130px">0.0m/s</div>
    <div class="speed" style="left:246px">0.0m/s</div>
    <div class="altitude">H 60m&nbsp; D 182m</div>
  </div>

  <div class="capture-info">
    <div class="muted">Format&nbsp; EV</div>
    <div>1185&nbsp; JPEG&nbsp; 0.0</div>
  </div>
  <div class="auto-badge">AUTO</div>
</main>
</body>
</html>
```